Kampfsport Außenwerbung
Zielgruppe
Kampfsportschule für Kinder, Jugendliche und Erwachsene. Sportarten: Kick-Boxen, Jiu-Jitsu und Tricking
Aufgabenstellung
Ich bräuchte für meine Schaufenster eine schöne Außenwerbung. Beworben werden sollen alle meine Sportarten. Ich lade meinen Flyer hoch, damit im ähnlichen Stil gearbeitet werden kann. Außerdem auch noch andere Beispiele an denen man sich orientieren kann, sowie mein Logo und meine Fensterfront.

```html
<!DOCTYPE html>
<html lang="de">
<head>
<meta charset="utf-8">
<title>Martial Arts Warb – Roll-up</title>
<link rel="stylesheet" href="https://fonts.googleapis.com/css2?family=Krona+One&family=Saira:wght@500;600&display=swap">
<style>
  :root {
    --red: #ed1c24;
    --dark-red: #a8201f;
    --crimson: #c01b2e;
    --black: #000000;
    --light-gray: #ececec;
    --white: #ffffff;
    --ink: #111111;
    --ink-soft: #333333;
    --stage: #b3b3b3;
  }
  html, body {
    margin: 0;
    width: 1200px;
    height: 1200px;
    overflow: hidden;
    background: var(--stage);
  }
  .rollup {
    position: absolute;
    left: 367px;
    top: 70px;
    width: 466px;
    height: 1061px;
    display: block;
  }
  .head-font { font-family: "Krona One", sans-serif; }
  .body-font { font-family: "Saira", sans-serif; font-weight: 600; }
  .brand-title { fill: var(--white); font-size: 46px; }
  .tagline-rotated { fill: var(--ink); font-size: 23px; }
  .section-title { fill: var(--red); font-size: 35px; }
  .discipline { fill: var(--ink); font-size: 16px; }
  .slogan { fill: var(--white); font-size: 35px; letter-spacing: 4px; }
  .leader { fill: var(--ink); font-size: 27px; }
  .address { fill: var(--ink); font-size: 19px; letter-spacing: 1.5px; }
  .info-title { fill: var(--ink); font-size: 20px; }
  .contact { fill: var(--ink-soft); font-size: 28px; letter-spacing: 2px; font-weight: 500; }
  .logo-name { fill: var(--white); font-size: 15px; }
</style>
</head>
<body>
<svg class="rollup" viewBox="0 0 582 1325" xmlns="http://www.w3.org/2000/svg">
  <defs>
    <clipPath id="top-section">
      <rect x="0" y="0" width="582" height="670"/>
    </clipPath>
    <linearGradient id="panel-fade" x1="0" y1="0" x2="0" y2="1">
      <stop offset="0" stop-color="#eef0ee"/>
      <stop offset="1" stop-color="#d9d9d9"/>
    </linearGradient>
    <radialGradient id="spot-glow" cx="0.5" cy="0.5" r="0.5">
      <stop offset="0" stop-color="#ffffff"/>
      <stop offset="0.25" stop-color="#9a9a9a"/>
      <stop offset="1" stop-color="#000000" stop-opacity="0"/>
    </radialGradient>
    <linearGradient id="photo-tone" x1="0" y1="0" x2="0" y2="1">
      <stop offset="0" stop-color="#c9a98a"/>
      <stop offset="0.25" stop-color="#f3f1ee"/>
      <stop offset="0.55" stop-color="#ede9e1"/>
      <stop offset="1" stop-color="#e4e4e4"/>
    </linearGradient>
  </defs>

  <rect class="base" width="582" height="1325" fill="var(--white)"/>

  <!-- hero section with diagonal bands -->
  <g class="hero" clip-path="url(#top-section)">
    <rect width="582" height="632" fill="var(--black)"/>
    <ellipse cx="335" cy="250" rx="130" ry="110" fill="url(#spot-glow)"/>
    <polygon fill="var(--dark-red)" points="0,-40 0,-15 700,685 700,660"/>
    <polygon fill="var(--red)" points="0,-15 0,60 700,760 700,685"/>
    <polygon fill="var(--light-gray)" points="0,60 0,170 700,870 700,760"/>
    <rect x="340" y="492" width="242" height="140" fill="var(--red)"/>
    <polygon fill="var(--red)" points="0,170 0,350 700,1050 700,870"/>
    <polygon fill="var(--dark-red)" points="0,350 0,380 700,1080 700,1050"/>
    <polygon class="gray-field" fill="var(--light-gray)" points="0,380 222,602 0,602"/>
    <polygon class="white-field" fill="var(--white)" points="0,602 222,602 290,670 0,670"/>
    <polygon class="base-bar" fill="var(--dark-red)" points="282,632 582,632 582,670 320,670"/>

    <!-- left red block with speed stripes -->
    <polygon fill="var(--red)" points="0,0 130,0 130,300 0,170"/>
    <g class="speed-stripes" stroke-width="9">
      <line x1="0" y1="45" x2="130" y2="175" stroke="var(--white)"/>
      <line x1="0" y1="70" x2="130" y2="200" stroke="var(--white)"/>
      <line x1="0" y1="95" x2="130" y2="225" stroke="var(--dark-red)"/>
      <line x1="0" y1="125" x2="130" y2="255" stroke="var(--white)"/>
    </g>

    <polygon class="corner-mark" fill="var(--red)" points="481,0 582,0 531,72"/>

    <g role="img" aria-label="Foto: Kind im weißen Karateanzug mit gelbem Gürtel in Kampfhaltung">
      <path d="M440,42 h110 q30 0 30 30 V632 H352 V195 q0 -30 30 -30 h28 V72 q0 -30 30 -30 Z" fill="url(#photo-tone)"/>
    </g>
  </g>

  <!-- brand name in place of logo -->
  <g class="brand-mark">
    <circle cx="291" cy="112" r="12" fill="var(--red)"/>
    <text class="head-font logo-name" x="291" y="152" text-anchor="middle" textLength="186" lengthAdjust="spacingAndGlyphs">Martial Arts WARB</text>
  </g>

  <!-- diagonal title -->
  <g class="diagonal-title head-font">
    <text class="brand-title" transform="translate(62,297) rotate(45)" textLength="318" lengthAdjust="spacingAndGlyphs">MARTIAL</text>
    <text class="brand-title" transform="translate(8,332) rotate(45)" textLength="388" lengthAdjust="spacingAndGlyphs">ARTS WARB</text>
    <text class="tagline-rotated" transform="translate(30,450) rotate(45)" textLength="240" lengthAdjust="spacingAndGlyphs">WIR MACHEN</text>
    <text class="tagline-rotated" transform="translate(2,475) rotate(45)" textLength="288" lengthAdjust="spacingAndGlyphs">KINDER SICHER</text>
  </g>

  <!-- disciplines -->
  <g class="disciplines head-font">
    <text class="section-title" x="31" y="712" textLength="372" lengthAdjust="spacingAndGlyphs">DISZIPLINEN:</text>
    <g fill="var(--red)">
      <polygon points="31,742 43,742 37,750"/>
      <polygon points="31,770 43,770 37,778"/>
      <polygon points="31,798 43,798 37,806"/>
      <polygon points="31,826 43,826 37,834"/>
    </g>
    <text class="discipline" x="47" y="751" textLength="320" lengthAdjust="spacingAndGlyphs">Kick-Boxen/Sportkarate</text>
    <text class="discipline" x="47" y="779" textLength="366" lengthAdjust="spacingAndGlyphs">Jiu-Jitsu Selbstverteidigung</text>
    <text class="discipline" x="47" y="807" textLength="101" lengthAdjust="spacingAndGlyphs">Tricking</text>
    <text class="discipline" x="47" y="835" textLength="209" lengthAdjust="spacingAndGlyphs">U25 Kick-Boxen</text>
  </g>

  <!-- slogan band -->
  <g class="slogan-band">
    <rect x="0" y="878" width="582" height="22" fill="var(--dark-red)"/>
    <rect x="0" y="900" width="582" height="387" fill="var(--red)"/>
    <polygon fill="var(--crimson)" points="0,892 149,1028 0,1072"/>
    <line x1="0" y1="892" x2="149" y2="1028" stroke="var(--white)" stroke-width="5"/>
    <text class="head-font slogan" x="149" y="949" textLength="326" lengthAdjust="spacingAndGlyphs">WIR MACHEN</text>
    <text class="head-font slogan" x="149" y="988" textLength="386" lengthAdjust="spacingAndGlyphs">KINDER STARK!</text>
  </g>

  <!-- right zigzag edge -->
  <g class="zigzag-edge">
    <polygon fill="var(--dark-red)" points="582,1070 515,1118 582,1160"/>
    <polygon fill="var(--dark-red)" points="582,1180 515,1228 582,1270"/>
    <polyline fill="none" stroke="var(--white)" stroke-width="5" points="582,1028 515,1078 582,1125 515,1172 582,1222 515,1268 582,1315"/>
  </g>

  <!-- contact panel -->
  <g class="contact-panel">
    <polygon fill="url(#panel-fade)" points="0,1072 149,1028 515,1028 515,1283 0,1283"/>
    <polygon fill="var(--crimson)" points="455,1283 507,1258 507,1283"/>
    <rect x="0" y="1283" width="582" height="5" fill="var(--dark-red)"/>
    <rect x="0" y="1288" width="582" height="37" fill="var(--red)"/>

    <text class="head-font leader" x="28" y="1097" textLength="450" lengthAdjust="spacingAndGlyphs">LEITUNG: JONAS WARB</text>
    <text class="body-font address" x="28" y="1131" textLength="458" lengthAdjust="spacingAndGlyphs">Am Werkhof 7c | 26400 Beispielstadt</text>
    <text class="head-font info-title" x="28" y="1176" textLength="410" lengthAdjust="spacingAndGlyphs">INFO &amp; PROBETRAINING:</text>

    <g class="icon-phone" fill="none" stroke="var(--red)" stroke-width="3">
      <circle cx="46" cy="1211" r="16"/>
      <path d="M39 1203 l4 -2 l3 6 l-3 2 q2 5 7 7 l2 -3 l6 3 l-2 4 q-11 1 -17 -17 z" fill="var(--red)" stroke="none"/>
    </g>
    <text class="body-font contact" x="88" y="1220" textLength="272" lengthAdjust="spacingAndGlyphs">0157/ 2468 1357</text>

    <g class="icon-mail" fill="none" stroke="var(--red)" stroke-width="2.5">
      <rect x="29" y="1246" width="35" height="23"/>
      <polyline points="29,1246 46.5,1261 64,1246"/>
      <line x1="29" y1="1269" x2="42" y2="1257"/>
      <line x1="64" y1="1269" x2="51" y2="1257"/>
    </g>
    <text class="body-font contact" x="88" y="1266" textLength="384" lengthAdjust="spacingAndGlyphs">info@martial-arts-warb.de</text>
  </g>
</svg>
</body>
</html>
```